Business Bench-marking brochure

Create a single page flyer for an account firm to advertise their Business Bench-marking product offering.

Style should follow new corporate image in development as per attached website psd.

The client likes the logo to always be on the RIGHT of publications.

Target Market(s)

Small - Medium sucessfully Business

Industry/Entity Type

Business

Colors
eb1f27

Requirements
Nice to have
• The client would like an image of a scales with Apples on both sides to be used -the idea being "comparing apples to apples"

```html
<!DOCTYPE html>
<html lang="en">
<head>
<meta charset="utf-8">
<title>Kestrel Business Consulting – Benchmarking Flyer</title>
<link href="https://fonts.googleapis.com/css2?family=Roboto:wght@300;400;500;700;900&display=swap" rel="stylesheet">
<style>
  :root {
    --brand-red: #eb1f27;
    --brand-red-dark: #b5121a;
    --ink: #555558;
    --ink-dark: #2a2a2c;
    --ink-soft: #6d6d70;
    --paper: #ffffff;
    --paper-fade: #ececee;
    --stage: #e4e4e6;
    --rule-grey: #5d6166;
  }
  * { margin: 0; padding: 0; box-sizing: border-box; }
  html, body {
    width: 988px; height: 1200px; overflow: hidden;
    background: var(--stage);
    font-family: "Roboto", Arial, sans-serif;
  }
  .flyer {
    position: absolute; left: 94px; top: 50px;
    width: 800px; height: 1100px;
    background: linear-gradient(180deg, var(--paper) 0%, var(--paper) 45%, var(--paper-fade) 100%);
    overflow: hidden;
  }
  .brand { position: absolute; left: 39px; top: 46px; color: var(--ink-dark); font-weight: 700; }
  .brand-name { font-size: 64px; line-height: 1; letter-spacing: -1px; }
  .brand-sub { font-size: 20px; line-height: 1; margin-top: 8px; letter-spacing: 0.3px; }
  .headline {
    position: absolute; left: 392px; top: 40px;
    color: var(--brand-red); font-weight: 700; font-size: 39px; line-height: 1.15;
  }
  .banner {
    position: absolute; left: 0; top: 175px; width: 505px; height: 98px;
    background: var(--brand-red);
    color: #fff; font-size: 31px; font-weight: 400; line-height: 1.22;
    text-align: center; padding-top: 10px;
  }
  .banner-fold { position: absolute; left: 505px; top: 175px; }
  .banner-rule {
    position: absolute; left: 523px; top: 199px; width: 277px; height: 11px;
    background: linear-gradient(180deg, #8b8f94, var(--rule-grey));
  }
  .questions {
    position: absolute; left: 42px; top: 292px;
    color: var(--ink); font-weight: 700; font-size: 29px; line-height: 44px;
  }
  .pain-points {
    position: absolute; left: 39px; top: 435px;
    color: var(--brand-red); font-weight: 500; font-size: 21px; line-height: 30px;
  }
  .pain-points p + p { margin-top: 4px; }
  .intro {
    position: absolute; left: 39px; top: 539px; width: 730px;
    color: var(--ink-soft); font-size: 12.5px; line-height: 17px; font-weight: 300;
  }
  .benefits-title {
    position: absolute; left: 39px; top: 608px;
    color: var(--brand-red); font-weight: 700; font-size: 28px;
  }
  .benefit { position: absolute; left: 39px; height: 33px; }
  .benefit svg { position: absolute; left: 0; top: 0; }
  .benefit span {
    position: absolute; left: 14px; top: 0; line-height: 33px;
    color: #fff; font-size: 15px; font-weight: 500; white-space: nowrap;
  }
  .closing {
    position: absolute; left: 39px; top: 846px; width: 480px;
    color: var(--ink-soft); font-size: 12.5px; line-height: 17px;
  }
  .closing p + p { margin-top: 8px; }
  .contact-label {
    position: absolute; left: 39px; top: 948px;
    color: var(--ink); font-size: 29px; font-weight: 300; letter-spacing: 0.5px;
  }
  .contact-phone {
    position: absolute; left: 37px; top: 982px;
    color: var(--ink); font-size: 52px; font-weight: 700; line-height: 1;
  }
  .portrait {
    position: absolute; left: 533px; top: 679px; width: 259px; height: 371px;
    background: linear-gradient(180deg, #d9c2b4 0%, #c7a895 28%, #3a3d44 45%, #1f2127 100%);
    border-radius: 120px 120px 0 0;
  }
  .footer {
    position: absolute; left: 0; top: 1050px; width: 800px; height: 50px;
    background: var(--brand-red);
    display: flex; align-items: center; justify-content: center; gap: 18px;
    color: #fff; font-weight: 700; font-size: 21px; letter-spacing: 0.3px;
  }
  .footer-dot { width: 12px; height: 12px; border-radius: 50%; background: #b9b9bb; }
</style>
</head>
<body>
<main class="flyer">
  <div class="brand">
    <div class="brand-name">KESTREL</div>
    <div class="brand-sub">BUSINESS CONSULTING</div>
  </div>

  <h1 class="headline">Does Your Business<br>Stack Up?</h1>

  <div class="banner">Help Your Business Operate<br>At Its Peak Performance</div>
  <svg class="banner-fold" width="18" height="18" viewBox="0 0 18 18"><polygon points="0,0 18,18 0,18" fill="var(--brand-red-dark)"/></svg>
  <div class="banner-rule"></div>

  <div class="questions">
    <p>How do you measure up?</p>
    <p>How does your business compare?</p>
    <p>Is your business performance good, bad or ugly?</p>
  </div>

  <div class="pain-points">
    <p>Ever wondered how your business compares to your competitors?</p>
    <p>Why you may be struggling to make a profit while other businesses<br>in your industry seem to have it all figured out?</p>
  </div>

  <p class="intro">By capturing the financial information and KPIs of your business we can compare your business to those within your industry. This enables you to be armed with the knowledge of how you can take corrective action by making informed decisions to save money and significantly enhance your overall performance</p>

  <h2 class="benefits-title">Benchmarking helps you:</h2>

  <div class="benefit" style="top:666px">
    <svg width="490" height="40" viewBox="0 0 490 40"><polygon points="0,0 452,0 465,16.5 452,33 0,33" fill="var(--brand-red)"/><polygon points="458,0 470,0 483,16.5 470,33 458,33 471,16.5" fill="var(--brand-red)"/></svg>
    <span>Identify where you can reduce costs and improve efficiencies</span>
  </div>
  <div class="benefit" style="top:713px">
    <svg width="390" height="40" viewBox="0 0 390 40"><polygon points="0,0 348,0 361,16.5 348,33 0,33" fill="var(--brand-red)"/><polygon points="354,0 366,0 379,16.5 366,33 354,33 367,16.5" fill="var(--brand-red)"/></svg>
    <span>Determine the productivity of your employees</span>
  </div>
  <div class="benefit" style="top:761px">
    <svg width="510" height="40" viewBox="0 0 510 40"><polygon points="0,0 473,0 486,16.5 473,33 0,33" fill="var(--brand-red)"/><polygon points="479,0 491,0 504,16.5 491,33 479,33 492,16.5" fill="var(--brand-red)"/></svg>
    <span>Highlight opportunities for improvement and innovative practices</span>
  </div>
  <div class="benefit" style="top:808px">
    <svg width="550" height="40" viewBox="0 0 550 40"><polygon points="0,0 515,0 528,16.5 515,33 0,33" fill="var(--brand-red)"/><polygon points="521,0 533,0 546,16.5 533,33 521,33 534,16.5" fill="var(--brand-red)"/></svg>
    <span>Discover opportunities for making your business more competitive</span>
  </div>

  <div class="closing">
    <p>To ensure your business is operating at its peak performance, call Kestrel Business Consulting for your detailed benchmark report.</p>
    <p>Full analysis of your financial statements, including KPIs, along with a meeting with Hannah Kestrel to identify areas to improve to help your business prosper.</p>
  </div>

  <div class="portrait" role="img" aria-label="Photo of a smiling consultant in a dark suit with arms folded"></div>

  <div class="contact-label">CONTACT US</div>
  <div class="contact-phone">02 5550 1847</div>

  <footer class="footer">
    <span>admin@kestrelconsulting.com.au</span>
    <span class="footer-dot"></span>
    <span>www.kestrelconsulting.com.au</span>
  </footer>
</main>
</body>
</html>
```